Desktop and Networking Support Course 9.17.25

Important the ad should not be very busy with the text taking up the major part of the ad .. please do not make the text so big that it takes up most of the ad..
Flyer Design Brief for Graphic Artist
also i am looking for something unique or creative that it will stand out .
Size & Layout:
Full Page with Bleed: 8” x 10.75” + 0.25” bleed on all sides.
Footer Space: Leave a 1-inch margin at the bottom for footer content (e.g., contact info, logo, or call-to-action).
Target Audience:
College-age students (around 24 years old)
Located in the USA
Interested in creative, professional, and career-building opportunities
Purpose:
To attract students to enroll in a college program
Flyer should be eye-catching, unique, and creative
Text must be clear and readable,
Design Style:
Use vector art, typography, or photography — your choice
If using photography, feature a white young professional USA citizen:
Wearing a white collared shirt
not with long hair
Creative Direction:
The flyer should stand out visually — something people would want to look at and keep
Showcase creativity and professionalism
Use bold colors, dynamic layout, or unexpected design elements to grab attention
Avoid clutter — keep the design balanced and clean
Text Suggestions (can be adjusted):
Footer,
please leave one inch on the bottom for the footer

```html
<!DOCTYPE html>
<html lang="en">
<head>
<meta charset="utf-8">
<title>Desktop &amp; Network Support Course Flyer</title>
<link href="https://fonts.googleapis.com/css2?family=Bebas+Neue&family=Figtree:wght@500;600;700;800&family=Montserrat:wght@400;700&family=Noto+Serif:ital@1&display=swap" rel="stylesheet">
<style>
  :root {
    --navy: #00247a;
    --navy-deep: #0a2d6e;
    --gold: #bb9404;
    --gold-light: #d9b40c;
    --white: #ffffff;
    --ink: #1c1c24;
    --sky: #dbe7ee;
  }
  * { margin: 0; padding: 0; box-sizing: border-box; }
  html, body { width: 927px; height: 1200px; overflow: hidden; background: var(--white); }
  .flyer { position: relative; width: 927px; height: 1200px; background: var(--white); overflow: hidden; }

  .tagline-tab { position: absolute; left: 0; top: 0; width: 927px; height: 87px; }
  .tagline-text {
    position: absolute; left: 0; width: 927px; top: 28px; text-align: center;
    font: 800 50px/1 "Figtree", sans-serif; color: var(--white); letter-spacing: -0.5px;
  }

  .cursor { position: absolute; top: 102px; width: 170px; height: 160px; }
  .cursor-left { left: 62px; }
  .cursor-right { left: 690px; transform: scaleX(-1); }

  .headline {
    position: absolute; left: 0; width: 927px; text-align: center; white-space: nowrap;
    font-family: "Bebas Neue", sans-serif; color: var(--gold); line-height: 1;
  }
  .headline-top { top: 92px; font-size: 206px; letter-spacing: -4px; }
  .headline-bottom { top: 253px; font-size: 206px; letter-spacing: 5px; }

  .course-band {
    position: absolute; left: 0; top: 430px; width: 927px; height: 63px; background: var(--navy);
    display: flex; align-items: center; justify-content: center; white-space: nowrap;
    font: 400 32px/1 "Montserrat", sans-serif; color: var(--white); letter-spacing: 2.5px;
  }
  .course-band strong { font-weight: 700; margin-right: 10px; }

  .skill-badge {
    position: absolute; left: 49px; top: 520px; width: 416px; height: 129px; border-radius: 22px;
    background: var(--gold); color: var(--white); text-align: center; white-space: nowrap;
    font: 400 58px/60px "Bebas Neue", sans-serif; padding-top: 6px;
  }

  .stat-figure {
    position: absolute; left: 46px; top: 655px; font: 400 119px/1 "Bebas Neue", sans-serif;
    color: var(--navy); letter-spacing: -1px; white-space: nowrap;
  }
  .stat-label {
    position: absolute; left: 216px; font-family: "Bebas Neue", sans-serif; line-height: 1;
    color: var(--navy); white-space: nowrap;
  }
  .stat-label-top { top: 670px; font-size: 43px; }
  .stat-label-bottom { top: 711px; font-size: 50px; letter-spacing: 0.5px; }
  .stat-rule { position: absolute; left: 216px; top: 707px; width: 245px; height: 2px; background: var(--gold); }

  .ranking-note {
    position: absolute; left: 47px; top: 772px; font: italic 21px/24px "Noto Serif", serif; color: var(--ink);
    white-space: nowrap;
  }

  .office-scene {
    position: absolute; left: 493px; top: 502px; width: 434px; height: 347px;
    background: linear-gradient(180deg, #f6f8fa 0%, #eef2f5 60%, #d9dde3 100%);
  }

  .benefits-band {
    position: absolute; left: 0; top: 849px; width: 927px; height: 218px;
    background: linear-gradient(90deg, var(--navy-deep) 0%, #123a80 50%, var(--navy) 100%);
  }
  .benefit-icon { position: absolute; top: 866px; width: 108px; height: 108px; }
  .benefit-label {
    position: absolute; top: 985px; width: 240px; text-align: center;
    font: 600 18px/22px "Figtree", sans-serif; color: var(--white);
  }
  .connector { position: absolute; width: 120px; height: 36px; }

  .options-pill {
    position: absolute; left: 49px; top: 1048px; width: 828px; height: 51px; border-radius: 26px;
    background: var(--gold); color: var(--white); display: flex; align-items: center; justify-content: center;
    font: 600 20.5px/1 "Figtree", sans-serif; white-space: nowrap;
  }
  .options-pill .divider { margin: 0 12px; }
</style>
</head>
<body>
<main class="flyer">

  <svg class="tagline-tab" viewBox="0 0 927 87" aria-hidden="true">
    <polygon points="190,0 736,0 702,87 225,87" fill="var(--navy)"/>
  </svg>
  <div class="tagline-text">YOUR CAREER IS</div>

  <svg class="cursor cursor-left" viewBox="0 0 148 146" aria-hidden="true">
    <g stroke="var(--gold)" stroke-width="6" stroke-linecap="round">
      <line x1="95" y1="8" x2="95" y2="28"/>
      <line x1="55" y1="20" x2="70" y2="34"/>
      <line x1="135" y1="20" x2="120" y2="34"/>
      <line x1="115" y1="55" x2="143" y2="55"/>
      <line x1="120" y1="74" x2="135" y2="88"/>
    </g>
    <path d="M92,52 L12,78 L40,94 L8,126 L26,142 L58,110 L72,138 Z" fill="var(--sky)" stroke="var(--white)" stroke-width="6" stroke-linejoin="round"/>
    <path d="M92,52 L58,110 L72,138 Z" fill="#c4d3dc"/>
  </svg>
  <svg class="cursor cursor-right" viewBox="0 0 148 146" aria-hidden="true">
    <g stroke="var(--gold)" stroke-width="6" stroke-linecap="round">
      <line x1="95" y1="8" x2="95" y2="28"/>
      <line x1="55" y1="20" x2="70" y2="34"/>
      <line x1="135" y1="20" x2="120" y2="34"/>
      <line x1="115" y1="55" x2="143" y2="55"/>
      <line x1="120" y1="74" x2="135" y2="88"/>
    </g>
    <path d="M92,52 L12,78 L40,94 L8,126 L26,142 L58,110 L72,138 Z" fill="var(--sky)" stroke="var(--white)" stroke-width="6" stroke-linejoin="round"/>
    <path d="M92,52 L58,110 L72,138 Z" fill="#c4d3dc"/>
  </svg>

  <h1>
    <span class="headline headline-top">JUST A</span>
    <span class="headline headline-bottom">CLICK AWAY</span>
  </h1>

  <div class="course-band"><strong>DESKTOP &amp; NETWORK</strong> SUPPORT COURSE</div>

  <div class="skill-badge">MASTER DESKTOP<br>OPERATING SYSTEMS</div>

  <div class="stat-figure">90%</div>
  <div class="stat-label stat-label-top">EMPLOYMENT RATE</div>
  <div class="stat-rule"></div>
  <div class="stat-label stat-label-bottom">CLASS OF 2024</div>

  <p class="ranking-note">Prepare for 3 of the Top 10 Tech Jobs<br>National Career Review 2025</p>

  <div class="office-scene" role="img" aria-label="Illustration of a young professional in a white shirt and tie working at a desk with a laptop, monitor and desk lamp in a bright office"></div>

  <section class="benefits-band" aria-label="Course benefits"></section>

  <svg class="benefit-icon" style="left:134px" viewBox="0 0 110 110" aria-hidden="true">
    <circle cx="55" cy="55" r="54" fill="var(--navy)"/>
    <circle cx="55" cy="55" r="46" fill="var(--gold-light)"/>
    <g fill="none" stroke="var(--white)" stroke-width="2.5" stroke-linecap="round" stroke-linejoin="round">
      <rect x="32" y="30" width="46" height="30"/>
      <polyline points="38,52 48,44 56,48 70,36"/>
      <circle cx="38" cy="68" r="5"/><circle cx="72" cy="68" r="5"/><circle cx="55" cy="74" r="5"/>
      <path d="M30,84 q8,-10 16,0 M64,84 q8,-10 16,0 M47,90 q8,-10 16,0"/>
    </g>
  </svg>
  <svg class="benefit-icon" style="left:406px" viewBox="0 0 110 110" aria-hidden="true">
    <circle cx="55" cy="55" r="54" fill="var(--navy)"/>
    <circle cx="55" cy="55" r="46" fill="var(--gold-light)"/>
    <g fill="none" stroke="var(--white)" stroke-width="2.5" stroke-linecap="round" stroke-linejoin="round">
      <circle cx="60" cy="48" r="20" stroke-dasharray="8 4"/>
      <circle cx="60" cy="48" r="12"/>
      <line x1="60" y1="41" x2="60" y2="49"/><circle cx="60" cy="54" r="0.8"/>
      <circle cx="44" cy="62" r="9"/>
      <line x1="37" y1="69" x2="27" y2="79"/>
    </g>
  </svg>
  <svg class="benefit-icon" style="left:676px" viewBox="0 0 110 110" aria-hidden="true">
    <circle cx="55" cy="55" r="54" fill="var(--navy)"/>
    <circle cx="55" cy="55" r="46" fill="var(--gold-light)"/>
    <g fill="none" stroke="var(--white)" stroke-width="2.5" stroke-linecap="round" stroke-linejoin="round">
      <circle cx="52" cy="38" r="10"/>
      <path d="M36,62 q16,-16 32,0"/>
      <rect x="34" y="64" width="36" height="20" rx="2"/>
      <line x1="28" y1="86" x2="76" y2="86"/>
      <circle cx="72" cy="56" r="10"/>
      <path d="M67,61 l9,-9"/>
    </g>
  </svg>

  <svg class="connector" style="left:264px; top:898px" viewBox="0 0 120 36" aria-hidden="true">
    <path d="M4,28 Q60,-10 116,28" fill="none" stroke="var(--white)" stroke-width="2"/>
    <circle cx="4" cy="28" r="4" fill="var(--white)"/><circle cx="116" cy="28" r="4" fill="var(--white)"/>
  </svg>
  <svg class="connector" style="left:535px; top:914px" viewBox="0 0 120 36" aria-hidden="true">
    <path d="M4,8 Q60,46 116,8" fill="none" stroke="var(--white)" stroke-width="2"/>
    <circle cx="4" cy="8" r="4" fill="var(--white)"/><circle cx="116" cy="8" r="4" fill="var(--white)"/>
  </svg>

  <p class="benefit-label" style="left:69px">Hands-On Desktop<br>&amp; Network Training</p>
  <p class="benefit-label" style="left:339px">Real-World<br>Troubleshooting Skills</p>
  <p class="benefit-label" style="left:607px">Ready<br>for IT Jobs</p>

  <div class="options-pill">IN-PERSON AND REMOTE OPTIONS<span class="divider">|</span>PARTIAL SCHOLARSHIPS OFFERED</div>

</main>
</body>
</html>
```